Etiketten für Honiggläser gesucht
sehr kreativer Entwurf, in dem alle umfangreichen Vorgaben berücksichtigt wurden. q4712 ist sehr service- und lösungsorientiert. Arbeitet sehr schnell und exzellent.
Zielgruppe
Wir sind eine junge Hobbyimkerei und produzieren unsere eigenen Honigsorten. Zielgruppe ist jeder, der Honig mag.
Aufgabenstellung
Das zu entwerfende Etiketten_Design soll grundsätzlich ein „absoluter Hingucker“ werden, einen hohen Wiedererkennungswert besitzen, edel erscheinen und die Hochwertigkeit des Produktes zum Ausdruck bringen.
Im engeren Sinn sollen zwei voneinander unabhängige Etikettenteile entworfen werden, die aber im Design eine Einheit bilden sollen:
Beim ersten Teil handelt es sich um den sogenannten Gewährverschluss; er verbindet den Deckel mit dem Glas und zerreißt beim ersten Öffnen des Deckels. Der Gewährverschluss soll etwa 2 cm breit und 8 cm lang sein, und unter anderem von unserem Firmenlogo (siehe Datei) geziert werden. Bei dem Logo darf die Grafik und der Hintergrund in der Farbe variieren, und der Schriftzug kann entfallen, andere Änderungen dürfen jedoch nicht vorgenommen werden. Das Logo kann bei Bedarf gerne in anderen Dateiformaten zur Verfügung gestellt werden.
Den zweiten Teil stellt das eigentliche Produktetikett dar. Für dieses gibt es keine Größen- und Formvorgaben, allerdings müssen folgende Inhalte Berücksichtigung finden: Die Daten des Imkers (bitte folgende Platzhalter verwenden „Firmenname“, „Vorname1 & Vorname2 Nachname“, „Straße + Hausnummer“, „PLZ + Ortsname“, „Internetseite“ und „Emailadresse“) sowie den Angaben „500g“, „Mindestens haltbar bis:“ (dahinter oder darunter bitte weißen Freiraum für den Stempelaufdruck des Datums lassen), „Trocken, dunkel und vor Wärme geschützt lagern!“, und – ganz wichtig – die „Honigsorte“ mit den vorangestellten Worten „feinster deutscher“ (, z.B. „feinster deutscher Rapshonig“).
Jede Honigsorte soll mit einer Farbe verknüpft werden, sodass der Kunde schnell erkennen kann um welche Honigsorte es sich im Glas handelt (beispielsweise gelb für Rapshonig, grün für Waldhonig, usw.). Dafür soll die jeweilige Honigsortenfarbe, in welcher Form auch immer, das Etikett oder einen bestimmten Bereich davon domini..

```html
<!DOCTYPE html>
<html lang="de">
<head>
<meta charset="utf-8">
<title>Himbeerhonig – Etikett</title>
<link href="https://fonts.googleapis.com/css2?family=Baloo+2:wght@700&family=Dancing+Script:wght@500&family=Open+Sans:wght@400;600&display=swap" rel="stylesheet">
<style>
  :root {
    --bg: #ffffff;
    --label: #ffffff;
    --variety: #c0134a;
    --frame-inner: #333333;
    --ink: #333333;
    --ink-soft: #555555;
    --brand: #a8672a;
    --script: #7a4a1e;
  }
  html, body {
    margin: 0;
    padding: 0;
    width: 1200px;
    height: 848px;
    overflow: hidden;
    background: var(--bg);
  }
  .canvas { display: block; width: 1200px; height: 848px; }
  .label-base { fill: var(--label); stroke: var(--variety); stroke-width: 11; }
  .label-inner-frame { fill: none; stroke: var(--frame-inner); stroke-width: 2.5; }
  .variety-name {
    font-family: "Baloo 2", "Open Sans", sans-serif;
    font-weight: 700; font-size: 64px; letter-spacing: 6px; fill: var(--variety);
  }
  .storage-note, .address {
    font-family: "Open Sans", sans-serif; font-weight: 400; font-size: 16px; fill: var(--ink-soft);
  }
  .address { font-size: 18px; letter-spacing: 1px; }
  .date-stamp-box { fill: var(--label); stroke: var(--ink); stroke-width: 2; }
  .net-weight { font-family: "Open Sans", sans-serif; font-size: 34px; fill: #111; }
  .brand-mark { fill: none; stroke: var(--brand); stroke-width: 4; }
  .brand-name {
    font-family: "Open Sans", sans-serif; font-weight: 600; font-size: 40px;
    letter-spacing: 6px; fill: var(--brand);
  }
  .tagline {
    font-family: "Dancing Script", cursive; font-weight: 500; font-size: 52px; fill: var(--script);
  }
</style>
</head>
<body>
<svg class="canvas" viewBox="0 0 1200 848" xmlns="http://www.w3.org/2000/svg">
  <defs>
    <path id="variety-arc" d="M 290 330 Q 600 100 910 330"/>
    <path id="tagline-arc" d="M 300 566 Q 560 740 905 515"/>
  </defs>

  <g class="product-label">
    <ellipse class="label-base" cx="600" cy="424" rx="446" ry="292"/>
    <ellipse class="label-inner-frame" cx="600" cy="424" rx="424" ry="271"/>

    <text class="variety-name" text-anchor="middle">
      <textPath href="#variety-arc" startOffset="50%">Himbeerhonig</textPath>
    </text>

    <g class="storage-info">
      <text class="storage-note" x="209" y="354">Trocken, dunkel und vor</text>
      <text class="storage-note" x="209" y="377">Wärme geschützt lagern</text>
      <text class="storage-note" x="209" y="404">Mindestens haltbar bis:</text>
      <rect class="date-stamp-box" x="209" y="418" width="175" height="40" rx="3"/>
      <text class="net-weight" x="244" y="500">500G.</text>
    </g>

    <g class="brand">
      <circle class="brand-mark" cx="600" cy="355" r="62"/>
      <text class="brand-name" x="600" y="475" text-anchor="middle">IMKEREI</text>
      <text class="brand-name" x="600" y="522" text-anchor="middle">HARMSEN</text>
    </g>

    <g class="address-block" text-anchor="end">
      <text class="address" x="982" y="348">Birkenstrasse 12</text>
      <text class="address" x="982" y="375">3014 Thun</text>
      <text class="address" x="982" y="402">www.imkerei-harmsen.de</text>
      <text class="address" x="982" y="430">@imkerei-harmsen.de</text>
    </g>

    <text class="tagline" text-anchor="middle">
      <textPath href="#tagline-arc" startOffset="50%">feinster deutscher Rapshonig</textPath>
    </text>
  </g>
</svg>
</body>
</html>
```